Membership Drive "End of Spring Sale"

Looking to run a Direct Debit Sale for November 2019 to boost membership number up. This is our slowest area for membership growth, many choose not to do direct debit, special is designed to increase numbers. Artwork will be display via social media (FB and Instagram) as well as in store. Artwork must be eye catching and direct to the customer. Customer should feel a sense of relief with monthly payments instead of one large payment.

Heading: "End of Spring Special"
Direct Debit
$39.95 per month
Terms and conditions apply"
*Offer End 30th November

Slogan:
"More Energy
More Atmosphere
Feel the Difference
Make the change now" can be placed where suits.

below are other promos we had designed on Artwork Hive along with potential photos to be included into this promo

Target Market(s)

Males and Females aged between 18 - 40

Industry/Entity Type

Fitness

Colors

Designer to choose colors to be used in the design.

Requirements
Must have
• Must emphasize "End of Spring Special" $39.95 per month and
• under neath strict terms and conditions apply
• Offer Ends 30th of November
• "All of our contact details"
• Address: 14 Marlow Rd Brindle Park 3187
• Ph: 9581 2706
• www.pulsarfit.com.au
• Design format must come in poster size A0 size, Instagram format, Facebook cover and 800 x 800 for the website
Nice to have
• With the photos attached at least one female and one male in the overall design. Lots of color in relation to Spring and artistic effects to catch peoples eyes.
• Also to include "Celebrating 49 years"

```html
<!DOCTYPE html>
<html lang="en">
<head>
<meta charset="utf-8">
<title>Pulsar Fit – End of Spring Special</title>
<link rel="stylesheet" href="https://fonts.googleapis.com/css2?family=Montserrat:ital,wght@0,500;0,600;0,700;1,600;1,700&family=Mrs+Saint+Delafield&display=swap">
<style>
  :root {
    --wall: #dedede;
    --ink-dark: #17211f;
    --ink-deep: #0f1615;
    --teal: #6fc6ad;
    --teal-soft: #4f9c89;
    --yellow: #f5c518;
    --white: #ffffff;
  }
  * { margin: 0; padding: 0; box-sizing: border-box; }
  html, body { width: 1200px; height: 800px; overflow: hidden; }
  body {
    background: var(--wall);
    font-family: "Montserrat", Arial, sans-serif;
    color: var(--white);
    position: relative;
  }
  .poster {
    position: absolute;
    left: 335px; top: 20px;
    width: 530px; height: 760px;
    background: linear-gradient(160deg, var(--ink-dark) 0%, var(--ink-deep) 100%);
    overflow: hidden;
  }
  .photo-area {
    position: absolute; inset: 0;
  }
  .brand {
    position: absolute; left: 73px; top: 50px;
    font-weight: 700; font-size: 26px; letter-spacing: 1px;
    color: var(--yellow); line-height: 1;
  }
  .headline-script {
    position: absolute; left: 170px; top: 200px; width: 220px;
    text-align: center;
    font-family: "Mrs Saint Delafield", cursive;
    font-size: 92px; color: var(--yellow); line-height: 1;
    transform: rotate(-8deg);
  }
  .headline {
    position: absolute; left: 155px; top: 262px;
    font-weight: 700; font-size: 54px; line-height: 1.05;
    letter-spacing: 0.5px;
  }
  .celebrating {
    position: absolute; left: 73px; top: 394px; width: 406px;
    font-weight: 700; font-size: 26px; color: var(--yellow);
    text-align: center; white-space: nowrap;
  }
  .rule {
    position: absolute; left: 73px; top: 432px;
    width: 406px; height: 3px; background: var(--white);
  }
  .price {
    position: absolute; left: 73px; top: 446px; width: 406px;
    font-weight: 700; font-size: 35px; text-align: center; white-space: nowrap;
  }
  .terms {
    position: absolute; left: 73px; top: 494px; width: 406px;
    font-weight: 500; font-size: 9.6px; text-align: center; white-space: nowrap;
  }
  .slogan {
    position: absolute; right: 51px; top: 538px;
    text-align: right; font-weight: 600; font-size: 17px; line-height: 1.32;
  }
  .slogan em { font-weight: 700; font-style: italic; }
  .cta {
    position: absolute; right: 51px; top: 615px;
    font-weight: 600; font-size: 22.5px; white-space: nowrap;
  }
  .cta-underline { position: absolute; left: 130px; top: 646px; }
  .website {
    position: absolute; right: 51px; top: 675px;
    font-weight: 700; font-size: 17px; color: var(--yellow);
  }
  .contact {
    position: absolute; right: 51px; top: 712px;
    display: flex; gap: 14px; align-items: center;
    font-weight: 500; font-size: 14.5px; white-space: nowrap;
  }
  .contact span { display: inline-flex; align-items: center; gap: 5px; }
</style>
</head>
<body>
<main class="poster">
  <svg class="photo-area" viewBox="0 0 530 760" role="img" aria-label="Photo of a female boxer in gloves throwing a punch, over a torn teal brush-stroke backdrop">
    <defs>
      <linearGradient id="tealWash" x1="0" y1="0" x2="1" y2="1">
        <stop offset="0" stop-color="#7fd3bb"/>
        <stop offset="0.6" stop-color="#5fb39d"/>
        <stop offset="1" stop-color="#3d7d6e"/>
      </linearGradient>
      <radialGradient id="figure" cx="0.62" cy="0.35" r="0.5">
        <stop offset="0" stop-color="#c9a58a" stop-opacity="0.55"/>
        <stop offset="0.5" stop-color="#2a3533" stop-opacity="0.5"/>
        <stop offset="1" stop-color="#2a3533" stop-opacity="0"/>
      </radialGradient>
    </defs>
    <polygon points="0,170 150,70 250,40 530,20 530,470 340,530 120,610 0,640" fill="url(#tealWash)"/>
    <rect x="0" y="0" width="530" height="760" fill="url(#figure)"/>
    <polygon points="0,0 250,0 120,55 0,130" fill="#1a2422" opacity="0.85"/>
    <polygon points="530,540 530,760 0,760 0,700 260,600" fill="#141c1b" opacity="0.9"/>
  </svg>

  <div class="brand">PULSAR FIT</div>

  <div class="headline-script">End of</div>
  <h1 class="headline">SPRING<br>SPECIAL</h1>

  <p class="celebrating">CELEBRATING 49 YEARS</p>
  <div class="rule"></div>
  <p class="price">$39.95/PER MONTH</p>
  <p class="terms">*TERMS AND CONDITIONS APPLY - OFFER END 30TH OF NOVEMBER</p>

  <p class="slogan">MORE <em>ENERGY</em><br>MORE <em>ATMOSPHERE</em><br><em>FEEL THE DIFFERENCE</em></p>

  <p class="cta">MAKE THE CHANGE NOW</p>
  <svg class="cta-underline" width="350" height="12" viewBox="0 0 350 12" aria-hidden="true">
    <path d="M2 7 Q90 2 180 5 T348 6 L346 10 Q200 12 4 11 Z" fill="var(--yellow)"/>
  </svg>

  <p class="website">WWW.PULSARFIT.COM.AU</p>

  <div class="contact">
    <span>
      <svg width="10" height="14" viewBox="0 0 10 14" aria-hidden="true"><path d="M5 0a5 5 0 0 0-5 5c0 3.6 5 9 5 9s5-5.4 5-9a5 5 0 0 0-5-5zm0 7a2 2 0 1 1 0-4 2 2 0 0 1 0 4z" fill="var(--white)"/></svg>
      14 MARLOW RD BRINDLE PARK 3187
    </span>
    <span>
      <svg width="13" height="13" viewBox="0 0 24 24" aria-hidden="true"><path d="M6.6 10.8a15.1 15.1 0 0 0 6.6 6.6l2.2-2.2a1 1 0 0 1 1-.25 11.4 11.4 0 0 0 3.6.57 1 1 0 0 1 1 1V20a1 1 0 0 1-1 1A17 17 0 0 1 3 4a1 1 0 0 1 1-1h3.5a1 1 0 0 1 1 1c0 1.25.2 2.45.57 3.57a1 1 0 0 1-.25 1z" fill="var(--white)"/></svg>
      9581 2706
    </span>
  </div>
</main>
</body>
</html>
```